EdTech Pellino

We am looking for complete redesign of our Mobile learning app and looking for a simple and best UI/UX design and ICON for our App. I have mentioned our app link below .
We sell Mobile app for students who prepares for Medical exams Educational apps.

We like a simple design , you can refer these apps
https://apps.storefrontdemo.test/us/app/vorlix-learn-languages-spanish-french-more/id504918273?mt=8

https://market.droidshelf.test/store/apps/details?id=fi.kx.android.tarvella&hl=en

our app:
IOS APP
https://apps.storefrontdemo.test/us/app/qorm-brevatel-rn-exam-prep-2017-edition/id1739025418?mt=8
Android
https://market.droidshelf.test/store/apps/details?id=com.pellinoworks.elearning.android.brevatelrn&hl=en

Target Market(s)

Our target audience are Medical student , age of 20 to 40

Industry/Entity Type

Medical

Font styles to use
Sans Serif

Colors
33a6d7
72c9bd
faa54b
f68d4d
3176b5

Requirements
Must have
• Icon and UX
Nice to have
• a better design for our test history as well

```html
<!DOCTYPE html>
<html lang="en">
<head>
<meta charset="utf-8">
<title>Medical-Surgical Quiz Screen</title>
<link rel="stylesheet" href="https://fonts.googleapis.com/css2?family=Arimo:wght@400;500&display=swap">
<style>
  :root {
    --page-bg: #f2f3f5;
    --screen-bg: #e9edf1;
    --brand-blue: #5a97e6;
    --card-bg: #ffffff;
    --text-main: #3a3a3a;
    --text-soft: #5f5f5f;
    --answer-green: #2a9d2a;
    --radio-line: #9a9a9a;
    --white: #ffffff;
  }
  * { box-sizing: border-box; margin: 0; padding: 0; }
  html, body {
    width: 1200px; height: 1200px; overflow: hidden;
    background: var(--page-bg);
    font-family: "Arimo", Arial, sans-serif;
  }
  .screen {
    position: absolute; left: 274px; top: 20px;
    width: 652px; height: 1160px;
    background: var(--screen-bg);
    overflow: hidden;
    box-shadow: 0 6px 30px rgba(0,0,0,0.12);
  }
  .app-bar {
    position: absolute; left: 0; top: 0; width: 100%; height: 115px;
    background: var(--brand-blue); color: var(--white);
  }
  .status-bar {
    position: absolute; left: 0; top: 10px; width: 100%; height: 24px;
    font-size: 19px; line-height: 24px;
  }
  .status-left { position: absolute; left: 15px; display: flex; align-items: center; gap: 6px; }
  .status-time { position: absolute; left: 0; width: 100%; text-align: center; }
  .status-right { position: absolute; right: 15px; display: flex; align-items: center; gap: 8px; }
  .title-row {
    position: absolute; left: 0; top: 56px; width: 100%; height: 44px;
  }
  .screen-title {
    position: absolute; left: 0; width: 100%; text-align: center;
    font-size: 30px; line-height: 44px; font-weight: 400;
  }
  .back-icon { position: absolute; left: 14px; top: 8px; }
  .menu-icon { position: absolute; right: 14px; top: 10px; }
  .card {
    position: absolute; left: 15px; width: 622px;
    background: var(--card-bg);
    box-shadow: 0 1px 3px rgba(0,0,0,0.08);
  }
  .question-card { top: 132px; height: 562px; padding: 16px 18px 0 18px; }
  .question-text {
    font-size: 25.5px; line-height: 34.2px; color: var(--text-main);
  }
  .question-text span, .rationale-text span { display: block; white-space: nowrap; }
  .answer-list { list-style: none; margin-top: 38px; }
  .answer {
    display: flex; align-items: center; height: 61.3px;
    font-size: 23px; color: var(--text-soft); white-space: nowrap;
  }
  .radio {
    width: 32px; height: 32px; border-radius: 50%;
    border: 2px solid var(--radio-line); margin-right: 17px; flex: none;
    position: relative;
  }
  .answer.is-correct { color: var(--answer-green); }
  .answer.is-correct .radio { border-color: var(--brand-blue); }
  .answer.is-correct .radio::after {
    content: ""; position: absolute; left: 7px; top: 7px;
    width: 14px; height: 14px; border-radius: 50%; background: var(--brand-blue);
  }
  .rationale-card { top: 709px; height: 336px; padding: 18px 18px 0 17px; }
  .rationale-title { font-size: 25.5px; line-height: 32px; color: var(--text-main); font-weight: 400; }
  .rationale-text {
    margin-top: 18px; font-size: 23px; line-height: 34.2px; color: var(--text-soft);
  }
  .nav-btn {
    position: absolute; border-radius: 50%;
    background: var(--brand-blue);
    box-shadow: 0 2px 4px rgba(0,0,0,0.25);
    display: flex; align-items: center; justify-content: center;
  }
  .nav-prev { left: 175px; top: 1089px; width: 45px; height: 45px; }
  .nav-study { left: 294px; top: 1079px; width: 65px; height: 65px; }
  .nav-next { left: 433px; top: 1089px; width: 45px; height: 45px; }
</style>
</head>
<body>
<main class="screen">
  <header class="app-bar">
    <div class="status-bar">
      <div class="status-left">
        <svg width="56" height="12" viewBox="0 0 56 12" aria-hidden="true">
          <circle cx="6" cy="6" r="5" fill="#fff"/><circle cx="17" cy="6" r="5" fill="#fff"/><circle cx="28" cy="6" r="5" fill="#fff"/>
          <circle cx="39" cy="6" r="4.3" fill="none" stroke="#fff" stroke-width="1.2"/><circle cx="50" cy="6" r="4.3" fill="none" stroke="#fff" stroke-width="1.2"/>
        </svg>
        <span>VELTA</span>
        <svg width="22" height="16" viewBox="0 0 22 16" aria-hidden="true">
          <path d="M1 5 A14 14 0 0 1 21 5" fill="none" stroke="#fff" stroke-width="2.2"/>
          <path d="M5 9 A9 9 0 0 1 17 9" fill="none" stroke="#fff" stroke-width="2.2"/>
          <path d="M8 12 L11 15 L14 12 A4.5 4.5 0 0 0 8 12Z" fill="#fff"/>
        </svg>
      </div>
      <div class="status-time">4:21 PM</div>
      <div class="status-right">
        <svg width="12" height="20" viewBox="0 0 12 20" aria-hidden="true">
          <path d="M1 6 L10 14 L5.5 18 V2 L10 6 L1 14" fill="none" stroke="rgba(255,255,255,0.6)" stroke-width="1.4"/>
        </svg>
        <span>100%</span>
        <svg width="42" height="18" viewBox="0 0 42 18" aria-hidden="true">
          <rect x="1" y="2" width="36" height="14" rx="3" fill="none" stroke="#fff" stroke-width="1.4"/>
          <rect x="3" y="4" width="32" height="10" rx="1.5" fill="#fff"/>
          <rect x="38.5" y="7" width="2.5" height="4" rx="1" fill="#fff"/>
        </svg>
      </div>
    </div>
    <div class="title-row">
      <svg class="back-icon" width="32" height="28" viewBox="0 0 32 28" aria-hidden="true">
        <path d="M30 14 H3 M13 4 L3 14 L13 24" fill="none" stroke="#fff" stroke-width="2.4" stroke-linecap="round" stroke-linejoin="round"/>
      </svg>
      <h1 class="screen-title">Medical-Surgical (75/100)</h1>
      <svg class="menu-icon" width="30" height="24" viewBox="0 0 30 24" aria-hidden="true">
        <path d="M1 3 H29 M1 12 H29 M1 21 H29" stroke="#fff" stroke-width="3"/>
      </svg>
    </div>
  </header>

  <section class="card question-card">
    <p class="question-text">
      <span>Lorem ipsum dolor sit amet, consectetur ing elit.</span>
      <span>Etiam vitae eros efficitur, finibus sapien et, porta</span>
      <span>libero. Integer facilisis massa dolor. vamus</span>
      <span>tempor enim sit amet lectus vehicula, eget luctus</span>
      <span>quam dignissim. Sed eu accumsan lacus. Nam et</span>
      <span>ullamcorper magna. Integer id diam varius arcu</span>
      <span>vestibulum porttitor?</span>
    </p>
    <ul class="answer-list">
      <li class="answer is-correct"><span class="radio"></span>Lorem ipsum dolor, consectetur adipiscing elit.</li>
      <li class="answer"><span class="radio"></span>Lorem ipsum dolor, consectetur adipiscing elit.</li>
      <li class="answer"><span class="radio"></span>Lorem ipsum dolor, consectetur adipiscing elit.</li>
      <li class="answer"><span class="radio"></span>Lorem ipsum dolor, consectetur adipiscing elit.</li>
    </ul>
  </section>

  <section class="card rationale-card">
    <h2 class="rationale-title">Rationale</h2>
    <p class="rationale-text">
      <span>Mauris ac molestie elit, id pharetra mauris. tesque</span>
      <span>habitant morbi tristique senectus et netus et da fames</span>
      <span>ac turpis egestas. Integer at erat id lorem consectetur</span>
      <span>tristique. Phasellus hendrerit metus velit, ut varius</span>
      <span>ipsum condimentum quis. Aliquam viverra orci sit</span>
      <span>amet risus volutpat vulputate. Vivamus vehicula</span>
      <span>pharetra ex eu tristique. Morbi sed fermentum velit.</span>
    </p>
  </section>

  <nav>
    <div class="nav-btn nav-prev" aria-label="Previous question">
      <svg width="14" height="20" viewBox="0 0 14 20" aria-hidden="true"><path d="M10 3 L3 10 L10 17" fill="none" stroke="#fff" stroke-width="1.8"/></svg>
    </div>
    <div class="nav-btn nav-study" aria-label="Study notes">
      <svg width="28" height="34" viewBox="0 0 28 34" aria-hidden="true">
        <rect x="6" y="2" width="18" height="26" rx="1.5" fill="#fff"/>
        <path d="M4 5 V31 H22" fill="none" stroke="#fff" stroke-width="2.4"/>
        <rect x="10" y="2" width="4" height="12" fill="#5a97e6"/>
      </svg>
    </div>
    <div class="nav-btn nav-next" aria-label="Next question">
      <svg width="14" height="20" viewBox="0 0 14 20" aria-hidden="true"><path d="M4 3 L11 10 L4 17" fill="none" stroke="#fff" stroke-width="1.8"/></svg>
    </div>
  </nav>
</main>
</body>
</html>
```